I need a business card design for a new dance business. I offer classical Indian dance tuition and also professional performances. I want to offer the community a variety of Indian dance experiences which include: group class and private tuition, school and preschool educational courses and workshops. dance theatre performances, community function workshops and performances, Kids Bollywood parties, wedding & conference performances, mouth percussion classes, Indian mythology/ dance costume and make up workshops.
The final design should communicate a feeling and impression of the vibrance and energy of Indian dance.
Updates
Hi Everyone,
Project Deadline Extended
Reason: I would like to refine a few changes to the details of this lovely design and we have run out of time!
Project Deadline Extended
Reason: Still waiting to hear back form designer re two possible changes to the card design. Tomorrow is the deadline and I have sent several messages but with no response. I need to see this through before selecting this lovely design.
Thank you.
Tessa
Industry/Entity Type
Preschool
Requirements
Must have
- The front of the business card should have the photo of me (my face and torso), surrounded entirely by a border of bright magenta (to match the magenta of my lipstick - it is the same as the magenta on my skirt in the second photo). Within the top border I want (perhaps yellow-gold) writing to say "Tessa Marlowe - Artistic Director" and within the bottom border it should read "Copper Lantern Indian Dance." If you turn the card on its side the left border should have my telephone number: 0417 862 049 and the right-hand border should read: copperlanternindiandance@velmora.com
The reverse of the card should be the orange of the dance costume
and I'd like the picture of my feet and legs to be on the right side of the back of the card as a side border. Centre-aligned on the orange background it should read (perhaps in dark magenta):
Indian dance classes + private tuition
School + preschool educational courses and workshops
Dance theatre performances
Community function workshops and performances
Children's Bollywood parties
Wedding + conference performances
Mouth percussion classes
Indian mythology and dance demonstration workshops
Dance costume and make-up workshops
Nice to have
- A lovely artistic but easy-to-read font would be nice.

```html
<!DOCTYPE html>
<html lang="en">
<head>
<meta charset="utf-8">
<title>Copper Lantern Indian Dance – Business Card</title>
<link rel="stylesheet" href="https://fonts.googleapis.com/css2?family=Arimo:wght@400;700&family=Pinyon+Script&display=swap">
<style>
  :root {
    --page: #ffffff;
    --orange-light: #f6a523;
    --orange-mid: #f39322;
    --orange-deep: #ef7021;
    --magenta: #b0166a;
    --magenta-deep: #8c0f52;
    --dark-magenta: #6a0c3c;
    --gold: #f5c94a;
    --white: #ffffff;
    --maroon: #6e1230;
    --skin: #e9c7b2;
  }
  * { box-sizing: border-box; margin: 0; padding: 0; }
  html, body { width: 1200px; height: 900px; overflow: hidden; background: var(--page); }
  body { position: relative; font-family: "Arimo", Arial, sans-serif; }

  .card {
    position: absolute;
    top: 173px;
    width: 309px;
    height: 555px;
    overflow: hidden;
    box-shadow: 2px 3px 5px rgba(0,0,0,0.28);
  }

  /* Front: portrait framed by a magenta border */
  .card--front {
    left: 281px;
    background: linear-gradient(180deg, var(--magenta) 0%, var(--magenta-deep) 100%);
  }
  .portrait-photo {
    position: absolute;
    left: 28px; top: 46px;
    width: 253px; height: 445px;
    background:
      radial-gradient(ellipse 40% 22% at 50% 26%, var(--skin) 0%, rgba(233,199,178,0) 100%),
      radial-gradient(ellipse 75% 40% at 50% 78%, var(--maroon) 0%, rgba(110,18,48,0) 100%),
      radial-gradient(ellipse 45% 30% at 75% 60%, var(--orange-mid) 0%, rgba(243,147,34,0) 100%),
      linear-gradient(90deg, var(--orange-light) 0%, var(--orange-deep) 100%);
  }
  .border-top {
    position: absolute; left: 0; right: 0; top: 0; height: 46px;
    display: flex; align-items: center; justify-content: center; gap: 6px;
    color: var(--gold); white-space: nowrap;
  }
  .director-name { font-family: "Pinyon Script", cursive; font-size: 27px; line-height: 1; }
  .director-role { font-size: 11.5px; letter-spacing: 0.3px; }
  .border-bottom {
    position: absolute; left: 0; right: 0; bottom: 0; height: 64px;
    display: flex; flex-direction: column; align-items: center; justify-content: center; gap: 4px;
    color: var(--gold); text-align: center;
  }
  .brand-name { font-size: 16.5px; font-weight: 400; letter-spacing: 0.6px; line-height: 1; }
  .credential { font-size: 10px; color: var(--white); line-height: 1; }
  .border-side {
    position: absolute; top: 46px; height: 445px; width: 28px;
    display: flex; align-items: center; justify-content: center;
    color: var(--white); font-size: 12.5px; white-space: nowrap;
  }
  .border-side span { display: block; transform: rotate(-90deg); }
  .border-side--left { left: 0; }
  .border-side--right { right: 0; }
  .border-side--right span { transform: rotate(90deg); }

  /* Back: orange with a leg-and-feet strip on the right */
  .card--back {
    left: 614px;
    width: 308px;
    background: linear-gradient(90deg, var(--orange-light) 0%, var(--orange-mid) 55%, var(--orange-deep) 100%);
  }
  .feet-photo {
    position: absolute;
    right: 0; top: 0;
    width: 92px; height: 555px;
    background:
      radial-gradient(ellipse 60% 10% at 50% 88%, #e0455a 0%, rgba(224,69,90,0) 100%),
      radial-gradient(ellipse 70% 35% at 50% 30%, var(--magenta) 0%, rgba(176,22,106,0) 100%),
      linear-gradient(180deg, var(--maroon) 0%, var(--orange-deep) 60%, var(--skin) 100%);
  }
  .services {
    position: absolute;
    left: 0; top: 0;
    width: 216px; height: 555px;
    padding: 0 10px;
    list-style: none;
    display: flex; flex-direction: column; justify-content: center; gap: 13px;
    text-align: center;
    color: var(--dark-magenta);
    font-size: 12px;
    line-height: 15.5px;
  }
</style>
</head>
<body>
  <section class="card card--front">
    <div class="border-top">
      <span class="director-name">Tessa Marlowe</span>
      <span class="director-role">– Artistic Director</span>
    </div>
    <div class="portrait-photo" role="img" aria-label="Portrait of the dancer's face and torso in classical costume with jewellery and flower headdress"></div>
    <div class="border-side border-side--left"><span>0417 862 049</span></div>
    <div class="border-side border-side--right"><span>copperlanternindiandance@velmora.com</span></div>
    <div class="border-bottom">
      <h1 class="brand-name">COPPER LANTERN INDIAN DANCE</h1>
      <p class="credential">Graduate of Kuchipudi classical Indian dance</p>
    </div>
  </section>

  <section class="card card--back">
    <ul class="services">
      <li>Indian dance classes<br>+ private tuition</li>
      <li>School + preschool educational<br>courses and workshops</li>
      <li>Dance theatre performances</li>
      <li>Community function workshops<br>and performances</li>
      <li>Children's Bollywood parties</li>
      <li>Wedding + conference<br>performances</li>
      <li>Mouth percussion classes</li>
      <li>Indian mythology and dance<br>demonstration workshops</li>
      <li>Dance costume and<br>make-up workshops</li>
    </ul>
    <div class="feet-photo" role="img" aria-label="Dancer's legs and hennaed feet with ankle bells beneath an orange and magenta costume"></div>
  </section>
</body>
</html>
```